7K packaging design

We are a wholesaler for Automotive Spare Parts in Jordan and Iraq market and we needs to import spare parts from China under our company private brand "7K"
The 7K brand’s product lines include Filtration, Braking Systems, Wheels, Wheel Bolts & Nuts, Shock Absorbers, Sensors, Cooling Systems, Axles and more.
The aim of the project is to unify the brand packaging across all the product lines , we will start by the brake pads then based on the approved design we will do the other products

Target Market(s)

Jordan , Iraq Market

Industry/Entity Type

Automotive spare parts

Requirements
Must have
• Name of the product :Ceramic brake pads specs : Superior stopping power Noise suppression Low Dust Technology Made in china
Nice to have
• Brake pad outline image on the box
Should not have
• Blue color

```html
<!DOCTYPE html>
<html lang="en">
<head>
<meta charset="utf-8">
<title>7K packaging design – Ceramic Brake Pads dieline</title>
<link rel="stylesheet" href="https://fonts.googleapis.com/css2?family=Exo+2:ital,wght@0,800;1,800&family=Roboto:wght@500&display=swap">
<style>
  :root {
    --red-bright: #ff0007;
    --red-mid: #d80008;
    --red-deep: #4a0000;
    --grey-light: #a6a6a6;
    --grey-mid: #7b7b7b;
    --grey-dark: #3c3c3c;
    --panel-dark: #333333;
    --cut-line: #2aa8d4;
    --white: #ffffff;
    --silver: #d9d9de;
  }
  html, body {
    margin: 0;
    padding: 0;
    width: 1091px;
    height: 1200px;
    overflow: hidden;
    background: var(--white);
  }
  .dieline { display: block; width: 1091px; height: 1196px; }
  .cut { fill: none; stroke: var(--cut-line); stroke-width: 1.4; }
  .title { font-family: "Exo 2", sans-serif; font-weight: 800; font-style: italic; fill: var(--white); }
  .brand-name { font-family: "Exo 2", sans-serif; font-weight: 800; font-style: normal; fill: var(--white); }
  .spec { font-family: "Roboto", Arial, sans-serif; font-weight: 500; fill: var(--white); }
  .icon { fill: none; stroke: var(--white); stroke-width: 2.4; }
  .panel-dark { fill: var(--panel-dark); }
</style>
</head>
<body>
<svg class="dieline" viewBox="0 0 1833 2010" xmlns="http://www.w3.org/2000/svg">
  <defs>
    <linearGradient id="redDiagonal" x1="0" y1="0" x2="0.35" y2="1">
      <stop offset="0" stop-color="#8a0003"/>
      <stop offset="0.55" stop-color="var(--red-mid)"/>
      <stop offset="1" stop-color="var(--red-bright)"/>
    </linearGradient>
    <linearGradient id="redFadeDown" x1="0" y1="0" x2="0" y2="1">
      <stop offset="0" stop-color="var(--red-bright)"/>
      <stop offset="0.45" stop-color="#e00006"/>
      <stop offset="1" stop-color="var(--red-deep)"/>
    </linearGradient>
    <linearGradient id="redFadeUp" x1="0" y1="1" x2="0" y2="0">
      <stop offset="0" stop-color="var(--red-deep)"/>
      <stop offset="0.6" stop-color="#c40006"/>
      <stop offset="1" stop-color="var(--red-bright)"/>
    </linearGradient>
    <linearGradient id="photoGrey" x1="0" y1="0" x2="1" y2="1">
      <stop offset="0" stop-color="var(--grey-mid)"/>
      <stop offset="0.5" stop-color="var(--grey-light)"/>
      <stop offset="1" stop-color="var(--grey-dark)"/>
    </linearGradient>
    <linearGradient id="featureBar" x1="0" y1="0" x2="1" y2="0">
      <stop offset="0" stop-color="#6e6e6e"/>
      <stop offset="1" stop-color="#a3a3a3"/>
    </linearGradient>
    <linearGradient id="silverBand" x1="0" y1="0" x2="1" y2="0">
      <stop offset="0" stop-color="#8d8d93"/>
      <stop offset="0.5" stop-color="var(--silver)"/>
      <stop offset="1" stop-color="#8d8d93"/>
    </linearGradient>
    <radialGradient id="padArt" cx="0.5" cy="0.5" r="0.6">
      <stop offset="0" stop-color="#e0000a"/>
      <stop offset="1" stop-color="#a00004"/>
    </radialGradient>

    <!-- Front face artwork, reused upside down on the lid flap -->
    <g id="frontFace">
      <rect class="car-photo" x="497" y="838" width="450" height="339" fill="url(#photoGrey)" role="img" aria-label="Photo of a silver sports car driving on a road"/>
      <polygon points="947,838 1336,838 1336,1113 815,1113" fill="url(#redDiagonal)"/>
      <polygon points="815,1113 1336,1113 1336,1177 780,1177" fill="url(#featureBar)"/>
      <polygon points="925,838 947,838 780,1177 758,1177" fill="url(#silverBand)"/>
      <rect class="pad-outline-art" x="940" y="862" width="365" height="230" rx="60" fill="url(#padArt)" opacity="0.85" role="img" aria-label="White line drawing of a pair of ceramic brake pads"/>

      <g class="brand-mark">
        <circle cx="545" cy="911" r="16" fill="var(--grey-light)"/>
        <text class="brand-name" x="570" y="934" font-size="64">7K</text>
      </g>

      <text class="title" font-size="38">
        <tspan x="523" y="1066">Ceramic</tspan>
        <tspan x="523" y="1098">Brake</tspan>
        <tspan x="523" y="1130">Pads</tspan>
      </text>

      <g class="feature stopping-power">
        <circle class="icon" cx="888" cy="1145" r="19"/>
        <circle class="icon" cx="888" cy="1145" r="8"/>
        <text class="spec" font-size="11"><tspan x="924" y="1138">SUPERIOR</tspan><tspan x="924" y="1149">STOPPING</tspan><tspan x="924" y="1160">POWER</tspan></text>
      </g>
      <g class="feature noise-suppression">
        <path class="icon" d="M1002 1138 h8 l10 -8 v30 l-10 -8 h-8 z"/>
        <path class="icon" d="M1024 1134 l8 -4 M1024 1145 h9 M1024 1156 l8 4"/>
        <text class="spec" font-size="11"><tspan x="1041" y="1143">NOISE</tspan><tspan x="1041" y="1154">SUPPRESSION</tspan></text>
      </g>
      <g class="feature low-dust">
        <circle class="icon" cx="1153" cy="1145" r="15" stroke-dasharray="3 4"/>
        <circle cx="1148" cy="1141" r="2" fill="var(--white)"/>
        <circle cx="1158" cy="1149" r="2" fill="var(--white)"/>
        <text class="spec" font-size="11"><tspan x="1178" y="1143">LOW DUST</tspan><tspan x="1178" y="1154">TECHNOLOGY</tspan></text>
      </g>
    </g>
  </defs>

  <!-- Lid tuck flaps -->
  <path class="tuck-flap" d="M497 103 L385 107 C290 112 205 250 196 350 C192 405 215 442 262 442 L497 442 Z" fill="url(#redDiagonal)"/>
  <path class="tuck-flap" d="M1336 103 L1448 107 C1543 112 1628 250 1637 350 C1641 405 1618 442 1571 442 L1336 442 Z" fill="url(#redDiagonal)"/>

  <!-- Lid front flap (upside down) -->
  <use href="#frontFace" transform="rotate(180 916.5 640)"/>

  <!-- Lid top -->
  <rect class="lid-top" x="497" y="442" width="839" height="396" fill="url(#redDiagonal)"/>
  <g class="lid-top-art" transform="rotate(180 916.5 640)">
    <rect class="pad-outline-art" x="880" y="505" width="418" height="268" rx="70" fill="url(#padArt)" opacity="0.85" role="img" aria-label="White line drawing of a pair of ceramic brake pads"/>
    <g class="brand-mark">
      <circle cx="555" cy="535" r="18" fill="var(--grey-light)"/>
      <text class="brand-name" x="583" y="561" font-size="72">7K</text>
    </g>
    <text class="title" x="538" y="687" font-size="30">Ceramic Brake Pads</text>
    <g class="feature-row">
      <circle class="icon" cx="555" cy="765" r="17"/>
      <circle class="icon" cx="555" cy="765" r="7"/>
      <text class="spec" font-size="10"><tspan x="587" y="758">SUPERIOR</tspan><tspan x="587" y="768">STOPPING</tspan><tspan x="587" y="778">POWER</tspan></text>
      <path class="icon" d="M654 759 h7 l9 -7 v26 l-9 -7 h-7 z"/>
      <path class="icon" d="M674 756 l7 -3 M674 765 h8 M674 774 l7 3"/>
      <text class="spec" font-size="10"><tspan x="690" y="763">NOISE</tspan><tspan x="690" y="773">SUPPRESSION</tspan></text>
      <circle class="icon" cx="788" cy="765" r="14" stroke-dasharray="3 4"/>
      <text class="spec" font-size="10"><tspan x="812" y="763">LOW DUST</tspan><tspan x="812" y="773">TECHNOLOGY</tspan></text>
    </g>
  </g>

  <!-- Dust flaps beside lid -->
  <path class="dust-flap" d="M100 515 H220 V499 H376 V515 H497 V838 H100 Z" fill="url(#redDiagonal)"/>
  <path class="dust-flap" d="M1336 515 H1456 V499 H1611 V515 H1732 V838 H1336 Z" fill="url(#redDiagonal)"/>

  <!-- Front row -->
  <rect class="side-photo" x="100" y="838" width="397" height="339" fill="url(#photoGrey)" role="img" aria-label="Photo of a silver sports car driving on a road"/>
  <g class="side-brand">
    <circle cx="230" cy="938" r="20" fill="var(--grey-light)"/>
    <text class="brand-name" x="260" y="966" font-size="82">7K</text>
  </g>
  <text class="title" x="298" y="1108" font-size="28" text-anchor="middle">Ceramic Brake Pads</text>
  <text class="spec" x="298" y="1147" font-size="15" text-anchor="middle">MADE IN CHINA</text>

  <use href="#frontFace"/>

  <rect class="side-photo" x="1336" y="838" width="396" height="339" fill="url(#photoGrey)" role="img" aria-label="Photo of a silver sports car driving on a road"/>

  <!-- Base row -->
  <rect class="panel-dark" x="100" y="1177" width="397" height="340"/>
  <rect class="panel-dark" x="1336" y="1177" width="396" height="340"/>
  <rect class="base" x="497" y="1177" width="839" height="396" fill="url(#redFadeDown)"/>
  <text class="title" x="916" y="1390" font-size="38" text-anchor="middle">Ceramic Brake Pads</text>
  <g class="disposal-icons">
    <path class="icon" d="M1245 1523 l-9 15 h8 M1245 1523 l9 15 M1236 1538 l-5 9 h9 M1254 1538 l5 9 h-10 M1240 1547 h10"/>
    <circle cx="1281" cy="1524" r="3" fill="var(--white)"/>
    <path class="icon" d="M1281 1529 v11 l-4 10 M1281 1535 l6 5"/>
    <rect class="icon" x="1289" y="1538" width="11" height="13"/>
  </g>

  <!-- Back row -->
  <rect class="panel-dark" x="100" y="1573" width="397" height="340"/>
  <rect class="panel-dark" x="1336" y="1573" width="396" height="340"/>
  <rect class="back" x="497" y="1573" width="839" height="340" fill="url(#redFadeDown)"/>

  <!-- Cut and fold lines -->
  <g class="cut">
    <path d="M497 103 L385 107 C290 112 205 250 196 350 C192 405 215 442 262 442 L497 442"/>
    <path d="M1336 103 L1448 107 C1543 112 1628 250 1637 350 C1641 405 1618 442 1571 442 L1336 442"/>
    <rect x="497" y="103" width="839" height="339"/>
    <rect x="497" y="442" width="839" height="396"/>
    <path d="M100 515 H220 V499 H376 V515 H497 V838 H100 Z"/>
    <path d="M1336 515 H1456 V499 H1611 V515 H1732 V838 H1336 Z"/>
    <rect x="100" y="838" width="1632" height="339"/>
    <path d="M497 838 V1177 M1336 838 V1177"/>
    <rect x="100" y="1177" width="397" height="340"/>
    <rect x="1336" y="1177" width="396" height="340"/>
    <rect x="497" y="1177" width="839" height="396"/>
    <rect x="228" y="1177" width="141" height="24"/>
    <rect x="1463" y="1177" width="142" height="24"/>
    <rect x="100" y="1573" width="1632" height="340"/>
    <path d="M497 1573 V1913 M1336 1573 V1913"/>
  </g>
</svg>
</body>
</html>
```